Zelmor Africa - Website Design Brief

Web Design Brief

ZELMOR AFRICA
WEBSITE DESIGN BRIEF

INTRODUCTION
ABOUT ZELMOR
• ZELMOR is a premier consulting firm that specialises in aiding global corporations and emerging businesses to enter and scale within Africa's dynamic markets. Through swift, actionable insights and innovative strategies, ZELMOR empowers clients to capitalise on Africa's untapped potential, thereby catering specifically to forward-thinking entities poised for exponential growth.

TASK DESCRIPTION
• Develop a 5-page website for ZELMOR.
• The primary goal is to present a clear and concise picture of our consulting firm, its Africa-centric experience, and its offerings to multinational clients looking for a professional partner to penetrate African markets or reclaim lost market share.

WEBSITE FRAMEWORK
Page Architecture:
• Home
o A powerful landing page that instantly communicates who ZELMOR is and what solutions it provides. Incorporate impactful visuals and calls-to-action.
• About
o A compelling narrative that illustrates ZELMOR's unique approach to consulting, dedication to Africa, and experience assisting multinational firms.
• Services
o A showcase of ZELMOR's successful projects and client testimonials. This page should build trust and credibility, demonstrating ZELMOR's ability to deliver exceptional results.
• Team
o Introduce up to 8 key team members, with each profile featuring a professional photo, name, title, and a brief bio showcasing the individual's skills, experiences, and contributions to ZELMOR's mission.
• Contact
o Clear and easy ways for visitors to contact ZELMOR for more information or to initiate a partnership.
• Footer
o Links to ZELMOR's social media profiles on Instagram and LinkedIn, along with a privacy policy.
o Social links
o Instagram: https://www.instagram.com/zelmorafrica/
o LinkedIn: https://www.linkedin.com/company/zelmorafrica/
o Privacy Policy
o Insert placeholder "lorem ipsum" text.
o Text will be provided with the revision round or ZELMOR will update text on site handover.

DESIGN INSPIRATION
• The website's design should evoke professionalism and elegance, with simple and clean lines inspired by site pages like:
o https://quendaro.example/
o https://quendaro.example/services/
o One aspect we particularly appreciate is how visitors can easily navigate by scrolling down to find what they're looking for and see everything they need to in an intuitive way on the home page
o What we don’t like about this site is how they navigate from the home page to other random pages – we like about to take you to the about page, and so on.

Branding Guidelines:
• See logo on Pixel Bazaar: Design #: 58170926
• We like the idea of the logo being black or white and have uploaded these options as well.
• Monochrome themes, with spots or splash of colour to highlight something is a style we appreciate.

Website Objectives and Goals:
• Our website's primary goal is to create a strong online presence, acting as a hub for potential clients to discover our credibility, reliability, and our ability to deliver exceptional results. It's essential that our website portrays professionalism, instils trustworthiness, and showcases our sincere dedication to Africa.

Target audience:
• ZELMOR's audience consists of businesses in mobile money, gaming, FMCG, beverage, and alcohol sectors, primarily Business Development Managers or Operations Managers who are seeking insight into their respective marketplaces.

Company Overview:
• ZELMOR stands out from the crowd as a consulting firm with a difference. Our dynamic team is fully dedicated to one mission: brand development within Africa.
• Unlike other companies that focus solely on online connectivity, we recognize the tremendous value in embracing the vibrant street culture that makes Africa so unique. Community engagement, empowerment, and expansion are at the forefront of everything we do.
• we recognize that unlocking business growth starts with a deep understanding of consumer behavior. It is this understanding that bridges the gap between companies and the communities that drive the cash economy. Our purpose is to reconnect businesses with the vibrant pulse of these essential local markets, injecting fresh vitality into their brands and propelling them towards resounding success in Africa.

Development to include:
• Basic SEO Setup:
o The website should be optimized for search engines, incorporating keywords, meta tags, and alt tags for images.
• Google Analytics Setup.
o To track website traffic and user behaviour for ongoing optimization.
• Google Crawling Setup
o The website needs to be easily indexed by Google, allowing it to appear in search results, and updated information effectively crawled by Google SEO and AHREFS scores.

PAGE CONTENT:
Home Page
• Background
o Option #1
o 4K video on home page, running on loop
o Bold Statement Text over Video
o Option #2
o Still Image
o Animated text making bold statement (e.g. our motto)

• Sections
o Contrast colour blocks or a way of making it clear that the next topic is a new topic.
o 5 sections
1. Home Main - Video + bold statement text
2. About - A paragraph and visual about us (lorem ipsum) that has a click through to our About Page (ignore how quendaro.example navigate, we think this is too complicated for our needs)
3. Services – communicated in some simple and powerful ways (we leave this open to you) – but keeping in mind it needs to be concise and professional.
4. Other - Something about our process that makes us unique (lorem ipsum text) and a placeholder image/animation.
5. Contact – a call-to-action button that takes you to our contact, but showcases a mobile number and email address.
6. Footer – as described in the previous section – placeholder for Instagram and LinkedIn only.

About Page
• Don’t reference quendaro.example for this page.
• Main Section
o Bold statements and images
• History Section
o A story about us and our past
• Final Section
o Some of our comments and final thoughts

Services Page
• How https://quendaro.example/services/ is laid out is great – we prefer a light theme.
• 6 - 8 x icons with headings and a brief description text box, and a read more drop down – all as placeholders to be edited later.
• For ease of direction for this page, look to the link shared above.

Team
• Add Placeholders for up to 8 team members (we only have 4 now):
o Image placeholder
o Name placeholder
o Title placeholder
o Short Bio (lorem ipsum)

Contact
• Clear and easy ways for visitors to contact ZELMOR for more information or to initiate a partnership.

• Insert placeholder "lorem ipsum" text, we will provide the text with our revision round.
o Ideally an easy form process that gives the user some options or dropdowns to complete before submission – up to 3 would be sufficient.
o Require their name and contact details.

NOTE: Images to follow:

Target Market(s)

ZELMOR's audience consists of businesses in mobile money, gaming, FMCG, beverage, and alcohol sectors, primarily Business Development Managers or Operations Managers who are seeking insight into their respective marketplaces.

Industry/Entity Type

ZELMOR is a premier consulting firm that specialises in aiding global corporations and emerging businesses to enter and scale within Africa's dynamic markets

Coding

Coded - Design and coding required

Number of Pages Required

5+ page

Font styles to use
Sans Serif
Other font styles liked:
• Poppins Font Family

Colors

Designer to choose colors to be used in the design.

Requirements
Must have
• The primary goal is to present a clear and concise picture of our consulting firm, and it's specialisation in Africa - smooth and crisp UI with animations or transitions that imply we know our way around tecchnology is always helpful - but a Clean and responsive UI is most important.
Nice to have
• Reactive and animated transitions through sections or pages - not overdone - adds a professional feel to the site
Should not have
• We don't want too many colours, and we don't want it too dark - we want a monochrome theme, with accents of colour when relevant

```html
<!DOCTYPE html>
<html lang="en">
<head>
<meta charset="utf-8">
<title>Zelmor Africa – Business Development Consulting</title>
<link rel="stylesheet" href="https://fonts.googleapis.com/css2?family=Poppins:wght@400;500;600;700;800&display=swap">
<style>
:root{
  --accent:#3a6ea5;
  --ink:#1c1c1c;
  --muted:#555;
  --page:#f2f2f2;
  --white:#fff;
  --footer:#1e1e1e;
  --hero-a:#2d4a6b;
  --hero-b:#6d8aa8;
}
*{box-sizing:border-box;margin:0;padding:0}
html,body{width:1200px;height:4850px;overflow:hidden}
body{font-family:"Poppins",sans-serif;color:var(--ink);background:var(--page);position:relative}
.abs{position:absolute}
.btn{position:absolute;display:flex;align-items:center;justify-content:center;font-weight:600;font-size:13px;background:var(--accent);color:var(--white);text-decoration:none}
.accent{color:var(--accent)}
.h2{position:absolute;font-weight:700;font-size:44px;line-height:54px;color:var(--ink)}
.lede{position:absolute;font-size:10.5px;line-height:19px;color:var(--muted)}

.site-header{position:absolute;left:0;top:0;width:1200px;height:68px;background:var(--white)}
.brand{position:absolute;left:111px;top:22px;font-weight:700;font-size:16px;letter-spacing:.3px}
.main-nav{position:absolute;left:497px;top:25px;display:flex;gap:0}
.main-nav a{font-size:11px;font-weight:500;color:var(--ink);text-decoration:none;margin-right:24px}

.hero{position:absolute;left:0;top:68px;width:1200px;height:535px;background:linear-gradient(180deg,#4e7396 0%,var(--hero-a) 55%,#3f6485 100%)}
.hero h1{position:absolute;left:111px;top:140px;font-size:42px;line-height:53px;font-weight:800;color:var(--white)}
.hero .btn{left:111px;top:333px;width:143px;height:46px;background:var(--white);color:var(--accent)}
.slide-arrow{position:absolute;top:228px;width:39px;height:34px;background:rgba(255,255,255,.35);display:flex;align-items:center;justify-content:center}
.scroll-hint{position:absolute;left:570px;top:440px;width:60px;text-align:center;color:var(--white);font-size:9px;font-weight:600}

.about-band{position:absolute;left:0;top:603px;width:1200px;height:141px;background:var(--white)}
.ph{position:absolute}
.about-img-a{left:113px;top:665px;width:415px;height:328px;background:linear-gradient(160deg,#9aa7b3,#6b5a4e 70%,#8f3b2e)}
.about-img-b{left:283px;top:831px;width:290px;height:230px;background:linear-gradient(135deg,#1f3f6e,#6f9ccc);border:6px solid var(--white)}

.svc{position:absolute;width:318px;overflow:hidden}
.svc .ph{left:0;top:0;width:100%;height:100%}
.svc .bar{position:absolute;left:0;bottom:0;width:100%;height:52px;background:rgba(30,30,30,.78);display:flex;align-items:center;padding-left:22px;gap:14px;color:var(--white);font-size:13px;font-weight:600}
.svc .ico{width:38px;height:38px;border-radius:50%;background:var(--white);display:flex;align-items:center;justify-content:center}

.quality{position:absolute;left:0;top:1935px;width:1200px;height:482px;background:linear-gradient(120deg,#4c6784,#33506d 45%,#5a6f86)}
.quality h2{position:absolute;left:0;top:130px;width:1200px;text-align:center;color:var(--white);font-size:45px;line-height:60px;font-weight:700}

.step{position:absolute;top:2684px;width:164px;height:148px;border:3px dashed var(--accent)}
.step .ph{left:45px;top:32px;width:70px;height:80px;border-radius:8px}
.step-label{position:absolute;top:2858px;width:164px;text-align:center;font-size:13px;font-weight:600;line-height:20px}
.chev{position:absolute;top:2754px}

.member{position:absolute;top:3146px;width:211px;height:255px;background:var(--white)}
.member .ph{left:0;top:0;width:211px;height:187px;background:linear-gradient(180deg,#e7e7e7,#b9aea2)}
.member .name{position:absolute;top:206px;width:100%;text-align:center;font-size:13px;font-weight:600}
.member .role{position:absolute;top:232px;width:100%;text-align:center;font-size:8px;color:var(--muted)}

.news{position:absolute;top:3606px;width:400px;height:495px}
.news .ph{left:0;top:0;width:100%;height:100%}
.news .txt{position:absolute;left:55px;top:343px;width:330px;color:var(--white)}
.news .cat{font-size:7px;font-weight:600;letter-spacing:.3px}
.news h3{font-size:18px;line-height:25px;font-weight:700;margin-top:6px}
.news p{font-size:8px;line-height:13px;margin-top:4px}
.news .date{font-size:7px;font-weight:600;margin-top:12px}
.news .more{font-size:7px;font-weight:700;margin-top:6px}

.contact{position:absolute;left:0;top:4246px;width:600px;height:407px;background:var(--accent)}
.contact h2{position:absolute;left:113px;top:44px;font-size:44px;font-weight:700;color:var(--white)}
.field{position:absolute;left:113px;width:377px;height:43px;border:1px solid rgba(255,255,255,.8);color:var(--white);font-size:10px;padding-left:26px;display:flex;align-items:center}
.contact .btn{left:113px;top:307px;width:141px;height:44px;background:var(--white);color:var(--accent)}
.contact-photo{left:600px;top:4246px;width:600px;height:407px;background:linear-gradient(120deg,#2f2b28,#7a6a60 55%,#c9b9c0)}

.site-footer{position:absolute;left:0;top:4653px;width:1200px;height:197px;background:var(--footer);color:var(--white)}
.site-footer .col{position:absolute;font-size:9px;line-height:18.8px}
.social{position:absolute;top:109px;width:28px;height:28px;border:1.5px solid var(--white);border-radius:50%}
.nl-input{position:absolute;left:820px;top:78px;width:267px;height:36px;border:1px solid rgba(255,255,255,.7);font-size:9px;padding-left:14px;display:flex;align-items:center}
.nl-btn{left:820px;top:127px;width:267px;height:34px;font-size:10px}
</style>
</head>
<body>

<header class="site-header">
  <div class="brand">ZELMOR AFRICA</div>
  <nav class="main-nav">
    <a href="#">Home</a><a href="#">About Us</a><a href="#">Services</a><a href="#">Team</a><a href="#">News</a><a href="#">Contact Us</a>
  </nav>
  <a class="btn" href="#" style="left:906px;top:17px;width:125px;height:34px;font-size:11px;font-weight:500">Get in Touch</a>
  <svg class="abs" style="left:1060px;top:24px" width="20" height="20" viewBox="0 0 20 20"><circle cx="8" cy="8" r="6" fill="none" stroke="#333" stroke-width="1.6"/><line x1="12.5" y1="12.5" x2="18" y2="18" stroke="#333" stroke-width="1.6"/></svg>
</header>

<section class="hero">
  <div class="ph" role="img" aria-label="City skyline with a suspension bridge over the river" style="left:0;top:0;width:100%;height:100%;background:linear-gradient(180deg,rgba(120,150,180,.4),rgba(30,60,90,.4))"></div>
  <h1>ZELMOR AFRICA<br>BUSINESS DEVELOPMENT<br>CONSULTING FIRM</h1>
  <a class="btn" href="#">Contact Us</a>
  <div class="slide-arrow" style="left:23px"><svg width="10" height="14"><polyline points="8,2 2,7 8,12" fill="none" stroke="#fff" stroke-width="1.5"/></svg></div>
  <div class="slide-arrow" style="left:1134px"><svg width="10" height="14"><polyline points="2,2 8,7 2,12" fill="none" stroke="#fff" stroke-width="1.5"/></svg></div>
  <div class="scroll-hint">
    <svg width="20" height="30" viewBox="0 0 20 30"><rect x="2" y="2" width="16" height="26" rx="8" fill="none" stroke="#fff" stroke-width="1.5"/><line x1="10" y1="7" x2="10" y2="12" stroke="#fff" stroke-width="1.5"/></svg>
    <div>Scroll Down</div>
  </div>
</section>

<section>
  <div class="about-band"></div>
  <div class="ph about-img-a" role="img" aria-label="Busy roadside market street with parked cars and umbrellas"></div>
  <div class="ph about-img-b" role="img" aria-label="Hands working with financial charts on a laptop screen"></div>
  <h2 class="h2" style="left:652px;top:682px">About <span class="accent">Zelmor Afria</span></h2>
  <p class="lede" style="left:652px;top:759px;width:395px">Lorem ipsum dolor sit amet, consectetur adipiscing elit. Duis tortor tortor, gravida eget ipsum quis, lobortis rutrum augue. Pellentesque eros elit, vulputate a tempus sed, congue ut erat. Mauris at metus dapibus turpis dictum condimentum quis vitae purus. Mauris lorem purus, maximus vel massa eget, dignissim consequat magna. Nam blandit lorem sit amet sodales vestibulum. Proin gravida nec orci eget pulvinar. Aenean nibh turpis, varius pretium ipsum vitae, viverra commodo enim.Vivamus lectus nulla, scelerisque vitae mi faucibus, sagittis varius leo. Vivamus in est sit amet libero consectetur viverra. Nam lobortis luctus risus.Vivamus lectus nulla, scelerisque vitae mi faucibus, sagittis varius leo. Vivamus in est sit amet libero consectetur viverra. Nam lobortis luctus risus.</p>
  <a class="btn" href="#" style="left:652px;top:1002px;width:141px;height:42px">Read More</a>
</section>

<section>
  <h2 class="h2" style="left:111px;top:1125px">Business<br>Consultation <span class="accent">Services</span></h2>
  <p class="lede" style="left:111px;top:1253px;width:700px">Lorem ipsum dolor sit amet, consectetur adipiscing elit, sed do eiusmod tempor incididunt ut labore et dolore magna aliqua. Quis ipsum suspendisse ultrices gravida. Risus commodo viverra maecenas accumsan lacus vel facilisis.</p>

  <div class="svc" style="left:113px;top:1324px;height:260px"><div class="ph" role="img" aria-label="Hands holding a glowing mobile phone" style="background:linear-gradient(150deg,#c3ccd6,#57708f)"></div><div class="bar"><span class="ico"><svg width="16" height="16"><rect x="4" y="1" width="8" height="14" rx="1.5" fill="none" stroke="#333" stroke-width="1.4"/></svg></span>Mobile Money</div></div>
  <div class="svc" style="left:441px;top:1324px;height:260px"><div class="ph" role="img" aria-label="Colleagues gathered around a laptop" style="background:linear-gradient(150deg,#d8dee4,#8a98a6)"></div><div class="bar"><span class="ico"><svg width="18" height="14"><rect x="1" y="2" width="16" height="10" rx="5" fill="none" stroke="#333" stroke-width="1.4"/></svg></span>Gaming Services</div></div>
  <div class="svc" style="left:767px;top:1324px;height:260px"><div class="ph" role="img" aria-label="Team reviewing charts on a tablet" style="background:linear-gradient(150deg,#4a4a4a,#b8b8b0)"></div><div class="bar"><span class="ico"><svg width="16" height="16"><circle cx="8" cy="8" r="6.5" fill="none" stroke="#333" stroke-width="1.4"/></svg></span>FMCG Services</div></div>
  <div class="svc" style="left:113px;top:1596px;height:264px"><div class="ph" role="img" aria-label="Two women tasting wine in a bar" style="background:linear-gradient(150deg,#7c7468,#3c352f)"></div><div class="bar"><span class="ico"><svg width="14" height="16"><rect x="4" y="1" width="6" height="14" rx="2" fill="none" stroke="#333" stroke-width="1.4"/></svg></span>Alcohol Sectors</div></div>
  <div class="svc" style="left:441px;top:1596px;height:264px"><div class="ph" role="img" aria-label="Friends enjoying drinks at a bar counter" style="background:linear-gradient(150deg,#6b5546,#2a2220)"></div><div class="bar"><span class="ico"><svg width="14" height="16"><path d="M3 2h8l-1 13H4z" fill="none" stroke="#333" stroke-width="1.4"/></svg></span>Beverage Services</div></div>
  <div class="svc" style="left:767px;top:1596px;height:264px"><div class="ph" role="img" aria-label="Smiling businessman in a blue suit with a colleague" style="background:linear-gradient(150deg,#d8c8ae,#4a5e7a)"></div><div class="bar"><span class="ico"><svg width="16" height="16"><circle cx="8" cy="8" r="6.5" fill="none" stroke="#333" stroke-width="1.4"/><circle cx="8" cy="8" r="2" fill="#333"/></svg></span>Operations Managers</div></div>
</section>

<section class="quality">
  <div class="ph" role="img" aria-label="Aerial view of a crowded open-air market with colourful umbrellas" style="left:0;top:0;width:100%;height:100%;background:linear-gradient(90deg,rgba(110,140,170,.3),rgba(80,60,90,.25))"></div>
  <h2>We Provide Best Quality<br>Business Services</h2>
  <svg class="abs" style="left:566px;top:282px" width="68" height="68" viewBox="0 0 68 68"><circle cx="34" cy="34" r="32" fill="#fff"/><circle cx="34" cy="34" r="26" fill="none" stroke="#3a6ea5" stroke-width="2"/><polygon points="28,23 46,34 28,45" fill="#3a6ea5"/></svg>
</section>

<section>
  <h2 class="h2" style="left:111px;top:2470px">Same Easy Way Of<br><span class="accent">Working Process</span></h2>
  <p class="lede" style="left:111px;top:2609px;width:700px">Lorem ipsum dolor sit amet, consectetur adipiscing elit, sed do eiusmod tempor incididunt ut labore et dolore magna aliqua. Quis ipsum suspendisse ultrices gravida. Risus commodo viverra maecenas accumsan lacus vel facilisis.</p>

  <div class="step" style="left:138px"><div class="ph" role="img" aria-label="Illustration of a man opening an account" style="background:linear-gradient(180deg,#cfe0f3,#6a9bd0)"></div></div>
  <div class="step" style="left:392px"><div class="ph" role="img" aria-label="Illustration of a calculator and money" style="background:linear-gradient(180deg,#f3dfa0,#6fbf8a)"></div></div>
  <div class="step" style="left:646px"><div class="ph" role="img" aria-label="Illustration of a team of three people" style="background:linear-gradient(180deg,#f3c4a8,#5b82c4)"></div></div>
  <div class="step" style="left:899px"><div class="ph" role="img" aria-label="Illustration of a rocket launching" style="background:linear-gradient(180deg,#f2a0a0,#e55a4e)"></div></div>

  <svg class="chev" style="left:334px" width="26" height="24"><polyline points="4,4 12,12 4,20" fill="none" stroke="#3a6ea5" stroke-width="3"/><polyline points="14,4 22,12 14,20" fill="none" stroke="#3a6ea5" stroke-width="3"/></svg>
  <svg class="chev" style="left:586px" width="26" height="24"><polyline points="4,4 12,12 4,20" fill="none" stroke="#3a6ea5" stroke-width="3"/><polyline points="14,4 22,12 14,20" fill="none" stroke="#3a6ea5" stroke-width="3"/></svg>
  <svg class="chev" style="left:840px" width="26" height="24"><polyline points="4,4 12,12 4,20" fill="none" stroke="#3a6ea5" stroke-width="3"/><polyline points="14,4 22,12 14,20" fill="none" stroke="#3a6ea5" stroke-width="3"/></svg>

  <div class="step-label" style="left:138px">Opening a Free<br>Account</div>
  <div class="step-label" style="left:392px">Make a Calculation<br>of Budget</div>
  <div class="step-label" style="left:646px">Consult With Our<br>Team</div>
  <div class="step-label" style="left:899px">Get Started<br>Now!</div>
</section>

<section>
  <h2 class="h2" style="left:0;top:2984px;width:1200px;text-align:center">Meet Out <span class="accent">Team Member</span></h2>
  <p class="lede" style="left:300px;top:3067px;width:600px;text-align:center">Lorem ipsum dolor sit amet, consectetur adipiscing elit, sed do eiusmod tempor incididunt ut labore et dolore magna aliqua. Quis ipsum suspendisse ultrices gravida. Risus commodo viverra maecenas accumsan lacus vel facilisis.</p>

  <div class="member" style="left:139px"><div class="ph" role="img" aria-label="Portrait of the founder"></div><div class="name">Dorian Kessly</div><div class="role">Founder &amp; CEO</div></div>
  <div class="member" style="left:375px"><div class="ph" role="img" aria-label="Portrait of the manager"></div><div class="name">Amara Veldt</div><div class="role">Manager</div></div>
  <div class="member" style="left:610px"><div class="ph" role="img" aria-label="Portrait of the senior consultant"></div><div class="name">Tobias Renwick</div><div class="role">Senior Consulting</div></div>
  <div class="member" style="left:846px"><div class="ph" role="img" aria-label="Portrait of the senior advisor"></div><div class="name">Lena Orsolay</div><div class="role">Senior Advisor</div></div>
</section>

<section>
  <h2 class="h2" style="left:111px;top:3453px">Our Latest <span class="accent">News</span></h2>
  <p class="lede" style="left:111px;top:3529px;width:600px">Lorem ipsum dolor sit amet, consectetur adipiscing elit, sed do eiusmod tempor incididunt ut labore et dolore magna aliqua. Quis ipsum suspendisse ultrices gravida. Risus commodo viverra maecenas accumsan lacus vel facilisis.</p>

  <article class="news" style="left:0"><div class="ph" role="img" aria-label="Traders at a street market stall" style="background:linear-gradient(180deg,#7e6a55,#3b3128 60%,#1c1a1a)"></div>
    <div class="txt"><div class="cat">NORVANE NEWS</div><h3>Norvane Names Marcus Ellery as Leader of Rapidly Growing Harbor Bay Markete</h3><div class="date">JUNE 5, 2023</div><div class="more">CONTINUE READING</div></div></article>
  <article class="news" style="left:400px"><div class="ph" role="img" aria-label="Black and white aerial view of a dense city street" style="background:linear-gradient(180deg,#9a9a9a,#4a4a4a 60%,#1f1f1f)"></div>
    <div class="txt"><div class="cat">INSIGHTS</div><h3>Bridging the GAAP: May 2023</h3><p>Lorem ipsum dolor sit amet, consectetur adipiscing elit, sed do eiusmod tempor incididunt ut labore et dolore magna aliqua. Quis ipsum suspendisse ultrices gravida.</p><div class="date">MAY 30, 2023</div><div class="more">CONTINUE READING</div></div></article>
  <article class="news" style="left:800px"><div class="ph" role="img" aria-label="Customers at a small shop counter" style="background:linear-gradient(180deg,#4f8a5a,#2c3a2c 60%,#1a1d1a)"></div>
    <div class="txt"><div class="cat">NORVANE NEWS</div><h3>Norvane Names Marcus Ellery as Leader of Rapidly Growing Harbor Bay Markete</h3><div class="date">JUNE 5, 2023</div><div class="more">CONTINUE READING</div></div></article>

  <a class="btn" href="#" style="left:529px;top:4152px;width:142px;height:43px">Read More</a>
</section>

<section>
  <div class="contact">
    <h2>Contact Us</h2>
    <div class="field" style="top:117px">Your Name</div>
    <div class="field" style="top:179px">Your Mail</div>
    <div class="field" style="top:242px">Phone Number</div>
    <a class="btn" href="#">Submit</a>
  </div>
  <div class="ph contact-photo" role="img" aria-label="Smiling man with earphone talking on a call"></div>
</section>

<footer class="site-footer">
  <div class="abs" style="left:111px;top:42px;font-weight:700;font-size:16px">ZELMOR AFRICA</div>
  <div class="abs" style="left:111px;top:76px;font-size:8px">© 2022 Zelmor Africa. All rights reserved.</div>
  <a class="social" href="#" aria-label="Social profile one" style="left:114px"></a>
  <a class="social" href="#" aria-label="Social profile two" style="left:156px"></a>
  <div class="col" style="left:346px;top:36px">Home<br>Services<br>Industries<br>One Team<br>News<br>Contact Us</div>
  <div class="col" style="left:471px;top:36px">412 Calloway Avenue<br>Suite 210<br>Brinmoor, ST 00000<br><br>hello@zelmorafrica.example<br>(555) 014-2290</div>
  <div class="col" style="left:674px;top:36px">Quick Links<br>What We Do<br>Articles<br>Success Stories</div>
  <div class="abs" style="left:820px;top:40px;font-size:16px;font-weight:600">Subscribr To Our Newsletter</div>
  <div class="nl-input">Enter your email</div>
  <a class="btn nl-btn" href="#">Subscribe Now</a>
</footer>

</body>
</html>
```